5x7 Outpour Promotional Card For a Church Conference

We need a 5x7 promotional card design for a church conference called Harvest Lantern Gathering with the theme "Outpour" The pictures and files are attached. We are open to original ideas. Fonts are from Microsoft Word and definitely are open for change. The attached files are just a suggestion. Let your creative ideas flow. The website of hlgathering.org must be listed on both sides. The pictures should not be photo shopped.
Updates

Industry/Entity Type

Church

Colors
3176b5
0293ce
33a6d7
85cae6
85acd3

Requirements
Nice to have
• Would be great to have the word "OUTPOUR" in a font that looks like it is dripping in water.
Should not have
• should not be whimsical or playful

```html
<!DOCTYPE html>
<html lang="en">
<head>
<meta charset="utf-8">
<title>Harvest Lantern Gathering – Outpour Card</title>
<link rel="stylesheet" href="https://fonts.googleapis.com/css2?family=Alfa+Slab+One&family=Arimo:wght@700&family=Caladea:ital,wght@0,400;0,700;1,400&display=swap">
<style>
  :root {
    --page: #ffffff;
    --sky-top: #1fb3e6;
    --sky-mid: #85cae6;
    --mist: #e6f4fb;
    --water: #0293ce;
    --water-deep: #0a4f9e;
    --navy: #0d2357;
    --ink-blue: #1f4ea0;
    --night: #06204a;
    --streak: #3176b5;
    --streak-light: #85acd3;
    --white: #ffffff;
    --yellow: #ffee3a;
    --photo-tone: #6f7f95;
  }
  * { box-sizing: border-box; margin: 0; padding: 0; }
  html, body { width: 1200px; height: 1000px; overflow: hidden; background: var(--page); }
  body { position: relative; font-family: "Caladea", Georgia, serif; }

  .card { position: absolute; width: 536px; height: 750px; overflow: hidden; text-align: center; }
  .card--front { left: 35px; top: 125px; }
  .card--back { left: 626px; top: 128px; }

  .backdrop { position: absolute; inset: 0; }
  .card--front .backdrop {
    background:
      radial-gradient(ellipse 60% 35% at 50% 48%, rgba(255,255,255,.85), rgba(255,255,255,0) 70%),
      linear-gradient(180deg, var(--sky-top) 0%, var(--sky-top) 24%, var(--sky-mid) 40%, var(--mist) 55%, var(--sky-mid) 72%, var(--water) 86%, var(--water-deep) 100%);
  }
  .card--back .backdrop {
    background:
      repeating-linear-gradient(90deg, rgba(133,172,211,.0) 0 14px, rgba(133,172,211,.22) 16px, rgba(133,172,211,0) 20px, rgba(49,118,181,.15) 31px, rgba(133,172,211,0) 36px),
      radial-gradient(ellipse 90% 18% at 50% 86%, rgba(133,202,230,.55), rgba(133,202,230,0) 70%),
      linear-gradient(180deg, var(--streak) 0%, #1a5a9a 30%, var(--night) 70%, #041735 100%);
  }

  .wordmark {
    position: absolute; left: 0; right: 0;
    font-family: "Arimo", Arial, sans-serif; font-weight: 700;
    color: var(--white); letter-spacing: 1px; line-height: 1;
  }
  .card--front .wordmark { top: 52px; font-size: 40px; }
  .card--back .wordmark { top: 102px; font-size: 38px; }

  .subtitle { position: absolute; left: 0; right: 0; font-style: italic; line-height: 1.1; }
  .card--front .subtitle { top: 120px; font-size: 29px; color: var(--ink-blue); }
  .card--back .subtitle { top: 145px; font-size: 32px; color: var(--white); }

  .theme {
    position: absolute; left: 0; right: 0;
    font-family: "Alfa Slab One", Georgia, serif; letter-spacing: 4px; line-height: 1;
    color: #2a7fc4;
    background: linear-gradient(180deg, #cfeefe 0%, #5fb8e8 35%, #0a4f9e 60%, #3aa2de 100%);
    -webkit-background-clip: text; background-clip: text; -webkit-text-fill-color: transparent;
    -webkit-text-stroke: 2px var(--white);
    filter: drop-shadow(2px 3px 2px rgba(0,20,60,.55));
  }
  .card--front .theme { top: 318px; font-size: 82px; }
  .card--back .theme { top: 16px; font-size: 74px; }

  .dates {
    position: absolute; left: 0; right: 0; top: 612px;
    font-family: "Alfa Slab One", Georgia, serif; font-size: 32px; color: var(--navy);
    -webkit-text-stroke: 1px var(--white); line-height: 1;
  }
  .site { position: absolute; left: 0; right: 0; font-weight: 700; line-height: 1; }
  .card--front .site { top: 662px; font-size: 19px; color: var(--navy); }
  .card--back .site { top: 720px; font-size: 18px; color: var(--white); }

  .prayer { position: absolute; left: 0; right: 0; top: 192px; color: var(--white); font-size: 16px; line-height: 17.5px; }
  .prayer__title { color: var(--yellow); font-weight: 700; font-size: 16px; margin-bottom: 3px; }

  .photo {
    position: absolute; background: linear-gradient(160deg, #b9c2cc, var(--photo-tone));
    border: 1px solid var(--white);
  }
  .photo--speaker-one { left: 217px; top: 299px; width: 111px; height: 111px; }
  .photo--speaker-two { left: 87px; top: 477px; width: 112px; height: 112px; }
  .photo--speaker-three { left: 354px; top: 477px; width: 114px; height: 114px; }

  .speaker { position: absolute; color: var(--white); font-style: italic; line-height: 1.05; text-shadow: 0 1px 3px rgba(0,0,0,.8); }
  .speaker__name { font-size: 19px; }
  .speaker__date { font-size: 14px; }
  .speaker--one { left: 118px; width: 300px; top: 423px; }
  .speaker--two { left: -7px; width: 300px; top: 600px; }
  .speaker--three { left: 261px; width: 300px; top: 600px; }

  .services { position: absolute; left: 0; right: 0; top: 652px; color: var(--white); font-size: 17px; line-height: 19.5px; text-shadow: 0 1px 2px rgba(0,0,0,.7); }
</style>
</head>
<body>
  <section class="card card--front">
    <div class="backdrop" role="img" aria-label="Soft blue sky with clouds, white doves and pouring light above rippling water"></div>
    <div class="wordmark">HARVEST LANTERN</div>
    <div class="subtitle">GATHERING<br>2015</div>
    <div class="theme">OUTPOUR!</div>
    <div class="dates">August 25-28</div>
    <div class="site">hlgathering.org</div>
  </section>

  <section class="card card--back">
    <div class="backdrop" role="img" aria-label="Deep blue waterfall streaks falling into splashing water"></div>
    <div class="theme">OUTPOUR!</div>
    <div class="wordmark">HARVEST LANTERN</div>
    <div class="subtitle">GATHERING</div>
    <div class="prayer">
      <div class="prayer__title">COMMUNITY PRAYER SERVICE</div>
      Tuesday, August 25 @ 7 PM<br>
      Living Waters Tabernacle<br>
      1450 Crestline Avenue<br>
      Brookhaven
    </div>

    <div class="photo photo--speaker-one" role="img" aria-label="Portrait photo of Evangelist Loretta Hayes"></div>
    <div class="speaker speaker--one">
      <div class="speaker__name">Evangelist Loretta Hayes</div>
      <div class="speaker__date">Wednesday August 26</div>
    </div>

    <div class="photo photo--speaker-two" role="img" aria-label="Portrait photo of Pastor Marcus Dell"></div>
    <div class="speaker speaker--two">
      <div class="speaker__name">Pastor Marcus Dell</div>
      <div class="speaker__date">Thursday August 27</div>
    </div>

    <div class="photo photo--speaker-three" role="img" aria-label="Portrait photo of Pastor Terrence Vale"></div>
    <div class="speaker speaker--three">
      <div class="speaker__name">Pastor Terrence Vale</div>
      <div class="speaker__date">Friday August 28</div>
    </div>

    <div class="services">
      Services Wednesday-Friday 7:30pm<br>
      Riverside Fellowship Church<br>
      3170 North Elm Grove Ave Westfield
    </div>
    <div class="site">hlgathering.org</div>
  </section>
</body>
</html>
```